KT Crewing business card

Require business card which includes:
Company name: KT CREWING PTY LTD
Email: Mick@ktcrewing.com.au
Phone: 0431 556 208
ACN: 517 238 649

slogan: Onsite Auto Electrician Labour hire

Details and logo on top side
Logo only on bottom side

colour codes : #F15A29 , #939598

Target Market(s)

Western Australia mining sector

Industry/Entity Type

Mining

Contact Information for Business Card

Require business card which includes: Company name: KT CREWING PTY LTD Email: Mick@ktcrewing.com.au Phone: 0431 556 208 ACN: 517 238 649 slogan: Onsite Auto Electrician Labour hire Details and logo on top side Logo only on bottom side colour codes : #F15A29 , #939598

Colors
EE7325
F08F49
F5BC92
FAE3D3
FDF4ED

Requirements
Must have
• double sided

```html
<!DOCTYPE html>
<html lang="en">
<head>
<meta charset="utf-8">
<title>KT Crewing – Business Card</title>
<link href="https://fonts.googleapis.com/css2?family=Arimo:wght@400;700&family=Michroma&display=swap" rel="stylesheet">
<style>
  :root {
    --page-bg: #e9e9e9;
    --card-bg: #323232;
    --brand-orange: #f15a29;
    --brand-grey: #939598;
    --text-light: #f2f2f2;
    --logo-deep: #1c1c1c;
  }
  * { margin: 0; padding: 0; box-sizing: border-box; }
  html, body {
    width: 1200px; height: 802px; overflow: hidden;
    background: var(--page-bg);
    font-family: "Arimo", Arial, sans-serif;
  }
  .card-set {
    position: absolute; top: 236px; left: 40px;
    display: flex; gap: 40px;
  }
  .card {
    position: relative; width: 540px; height: 330px;
    background: var(--card-bg);
    box-shadow: 0 6px 18px rgba(0,0,0,0.18);
  }

  /* Front side */
  .card-front .brand-block {
    position: absolute; left: 40px; top: 0; bottom: 0; width: 230px;
    display: flex; align-items: center; gap: 12px;
  }
  .brand-square {
    width: 22px; height: 22px; background: var(--brand-orange); flex: none;
  }
  .brand-name {
    font-weight: 700; font-size: 34px; color: var(--brand-orange);
    letter-spacing: 0.5px; white-space: nowrap;
  }
  .divider {
    position: absolute; left: 280px; top: 95px; width: 1px; height: 140px;
    background: var(--brand-grey);
  }
  .details {
    position: absolute; left: 305px; top: 98px;
    color: var(--text-light); font-size: 15px; line-height: 1.35;
  }
  .person-name {
    color: var(--brand-orange); font-weight: 700; font-size: 17px;
    letter-spacing: 0.3px;
  }
  .person-role { margin-bottom: 14px; }
  .acn-label { color: var(--brand-orange); font-weight: 700; }
  .contact-line { display: flex; align-items: center; gap: 8px; }
  .contact-line svg { width: 13px; height: 13px; flex: none; }

  /* Back side */
  .card-back .brand-mark {
    position: absolute; left: 0; right: 0; top: 105px;
    text-align: center;
    font-weight: 700; font-size: 60px; color: var(--logo-deep);
    letter-spacing: 1px;
  }
  .card-back .slogan {
    position: absolute; left: 0; right: 0; bottom: 60px;
    text-align: center;
    font-family: "Michroma", Arial, sans-serif;
    font-size: 13px; color: var(--brand-orange);
    text-transform: uppercase; letter-spacing: 1px;
  }
</style>
</head>
<body>
  <main class="card-set">
    <section class="card card-front" aria-label="Business card front">
      <div class="brand-block">
        <span class="brand-square"></span>
        <span class="brand-name">KT Crewing</span>
      </div>
      <div class="divider"></div>
      <div class="details">
        <p class="person-name">RYAN COLE</p>
        <p class="person-role">Manager</p>
        <p class="acn"><span class="acn-label">ACN</span> 517 238 649</p>
        <p class="contact-line">
          <svg viewBox="0 0 16 16" aria-hidden="true"><path fill="#f15a29" d="M3.5 1.5l2.4 0 1.1 3.2-1.6 1.2a8 8 0 0 0 4.7 4.7l1.2-1.6 3.2 1.1v2.4c0 .8-.7 1.5-1.5 1.5A12.5 12.5 0 0 1 2 3c0-.8.7-1.5 1.5-1.5z"/></svg>
          0431 556 208
        </p>
        <p class="contact-line">
          <svg viewBox="0 0 16 16" aria-hidden="true"><rect x="1" y="3" width="14" height="10" fill="#f15a29"/><path d="M1.5 3.5L8 9l6.5-5.5" fill="none" stroke="#323232" stroke-width="1.4"/></svg>
          Mick@ktcrewing.com.au
        </p>
      </div>
    </section>

    <section class="card card-back" aria-label="Business card back">
      <p class="brand-mark">KT Crewing</p>
      <p class="slogan">Onsite Auto Electrician Labour Hire</p>
    </section>
  </main>
</body>
</html>
```